TQ Regulatory Partners - Biz Card - Re-do

I would like a re-do on my business card.

See my Internet site - tqregpartners.com

1) Remove direct phone line.
2) Add company moto - integrity, diligence, and excellence
3) Add Consulting Services listing:
-Benefit Technology
-ERISA Compliance
-Contract/Vendor Management
-Human Resource/Payroll
-Medical/Prescription Drug
-Integrated Leave of Absence

Target Market(s)

Employee benefit consulting and insurance purchasers, Usually human resource executives

Industry/Entity Type

Human Resource

Contact Information for Business Card

Same business card color scheme, logo,

Font styles to use
Sans Serif

Requirements
Must have
• Same color scheme and logo. Remove direct phone number. Keep all numbers, internet address.

```html
<!DOCTYPE html>
<html lang="en">
<head>
<meta charset="utf-8">
<title>TQ Regulatory Partners – Business Card</title>
<link rel="stylesheet" href="https://fonts.googleapis.com/css2?family=Libre+Bodoni:wght@400;700&display=swap">
<style>
  :root {
    --backdrop: #3a3a3d;
    --card-grey: #606167;
    --card-white: #ffffff;
    --maroon: #6b1d47;
    --ink-grey: #55565b;
    --ink-dark: #333338;
    --white: #ffffff;
  }
  * { box-sizing: border-box; margin: 0; padding: 0; }
  html, body {
    width: 1200px; height: 1000px; overflow: hidden;
    background: var(--backdrop);
    font-family: "Libre Bodoni", "Bodoni Moda", Georgia, serif;
  }
  .stage { position: relative; width: 1200px; height: 1000px; }
  .card {
    position: absolute; left: 290px; width: 620px; height: 354px;
    border-radius: 24px; overflow: hidden;
    box-shadow: 0 18px 40px rgba(0,0,0,.45);
  }
  /* back */
  .card-back { top: 90px; background: var(--card-grey); text-align: center; }
  .brand-dot {
    display: block; margin: 0 auto; border-radius: 50%; background: var(--maroon);
  }
  .card-back .brand-dot { width: 78px; height: 78px; margin-top: 80px; }
  .card-back .brand-name {
    margin-top: 14px; font-size: 40px; color: var(--white); letter-spacing: .3px;
  }
  .motto {
    margin-top: 12px; font-size: 17px; color: var(--white); letter-spacing: .6px;
  }
  .motto .sep {
    display: inline-block; width: 9px; height: 9px; border-radius: 50%;
    background: var(--maroon); margin: 0 7px; vertical-align: middle;
  }
  /* front */
  .card-front { top: 520px; background: var(--card-white); }
  .card-front .brand-dot { width: 76px; height: 76px; margin-top: 26px; }
  .card-front .brand-name {
    text-align: center; margin-top: 8px; font-size: 38px; color: var(--ink-grey);
  }
  .person {
    text-align: center; margin-top: 10px; font-size: 16px; color: var(--ink-grey);
  }
  .person-name { font-weight: 700; font-size: 21px; color: var(--maroon); margin-right: 6px; }
  .contact {
    display: flex; justify-content: center; margin-top: 12px;
    font-size: 13.5px; color: var(--ink-dark); line-height: 1.45;
  }
  .contact-office { text-align: right; padding-right: 12px; border-right: 1px solid var(--ink-grey); }
  .contact-direct { padding-left: 12px; }
  .contact-line { display: flex; align-items: center; gap: 5px; }
  .contact-office .contact-line { justify-content: flex-end; }
  .contact-line svg { width: 12px; height: 12px; fill: var(--ink-dark); }
  .web { color: var(--maroon); font-weight: 700; }
  .services {
    position: absolute; left: 0; right: 0; bottom: 0; height: 66px;
    background: var(--maroon); color: var(--white);
    font-size: 14px; text-align: center; line-height: 1.5; padding-top: 9px;
    letter-spacing: .3px;
  }
</style>
</head>
<body>
<main class="stage">
  <section class="card card-back">
    <span class="brand-dot"></span>
    <h1 class="brand-name">TQ Regulatory Partners</h1>
    <p class="motto">Integrity<span class="sep"></span>Diligence<span class="sep"></span>Excellence</p>
  </section>

  <section class="card card-front">
    <span class="brand-dot"></span>
    <h2 class="brand-name">TQ Regulatory Partners</h2>
    <p class="person"><span class="person-name">Daniel Harlow</span>President</p>
    <div class="contact">
      <div class="contact-office">
        <p>118 Lakeview Street NE, Suite 300</p>
        <p>Riverton, MI 49210</p>
        <p class="contact-line">555.210.4471
          <svg viewBox="0 0 24 24" aria-hidden="true"><path d="M6.6 10.8a15 15 0 0 0 6.6 6.6l2.2-2.2c.3-.3.7-.4 1-.2 1.1.4 2.3.6 3.6.6.6 0 1 .4 1 1V20c0 .6-.4 1-1 1A17 17 0 0 1 3 4c0-.6.4-1 1-1h3.5c.6 0 1 .4 1 1 0 1.3.2 2.5.6 3.6.1.3 0 .7-.2 1z"/></svg>
        </p>
      </div>
      <div class="contact-direct">
        <p class="contact-line">
          <svg viewBox="0 0 24 24" aria-hidden="true"><path d="M6 3h12v5H6zM3 9h18v9h-3v3H6v-3H3zm5 6v4h8v-4z"/></svg>555.210.4472</p>
        <p class="contact-line">
          <svg viewBox="0 0 24 24" aria-hidden="true"><path d="M2 5h20v14H2zm2 2v.5l8 5 8-5V7z"/></svg>dharlow@tqregpartners.com</p>
        <p class="contact-line web">
          <svg viewBox="0 0 24 24" aria-hidden="true"><path d="M12 2a10 10 0 1 0 0 20 10 10 0 0 0 0-20zm0 2c1 1.3 1.8 3.6 2 6h-4c.2-2.4 1-4.7 2-6zM4.1 11h3.9c.1 2.3.7 4.4 1.6 6A8 8 0 0 1 4.1 11zm0-2a8 8 0 0 1 5.5-6c-.9 1.6-1.5 3.7-1.6 6zm5.9 2h4c-.2 2.4-1 4.7-2 6-1-1.3-1.8-3.6-2-6zm6 0h3.9a8 8 0 0 1-5.5 6c.9-1.6 1.5-3.7 1.6-6zm0-2c-.1-2.3-.7-4.4-1.6-6a8 8 0 0 1 5.5 6z"/></svg>www.tqregpartners.com</p>
      </div>
    </div>
    <div class="services">
      <p>Benefit Technology | ERISA Compliance | Contract/Vendor Management</p>
      <p>| Human Resource/Payroll | Medical/Prescription Drug | Integrated Leave of Absence</p>
    </div>
  </section>
</main>
</body>
</html>
```